Yacht, Boats, Watersports company needs a redesign of business card

Hello Designers!
We are a Boat dealership company that sells fun in the water, we sell boats, Yachts, Kayaks and also yacht WaterSport toys. We are looking to redesign our business cards in to something a little bit more sophisticated. in a way that we can make better use of our company colors. I'm attaching a zipped file containing the company 3 sets of company logo which one is an horizontal another one is a vertical and also a chromed 3d logo. Also is included two set of business cards that we use and also some designs that i think it's interesting. We use PMS 2026c Orange and PMS 7687C Blue. I would like to see at least two different options with the orange as accent and also using blue as an accent color. It's really important for the business cards to have a font option and size that is legible to most people. Our current website is wwww.corvellamarine.com. Please visit if you want to have a better feeling of the Boat dealership
You can send Single sided or double side options. We are now using single sided but we may be open for a double side option if we really like the design.
Target Market(s)
Marine, boat sales, yacht sales, water toys sales/
Contact Information for Business Card
Name: Dale Pritchett
Address: 718 West Halden Lane,
Dania Beach, FL 33019
Phone: 954-382-7146
Fax: 954:382-7139
Cell: 954-451-8320
Email: 212@corvellamarine.com
Website: corvellamarine.com
Requirements
Must have
- the current information of the business card provided.
logo
use the PMS Colors
Nice to have
- a touch of elegance and sophistication but simple
Should not have
- should not have any typography that is hard to read, the card should be simple but yet sophisticated.

```html
<!DOCTYPE html>
<html lang="en">
<head>
<meta charset="utf-8">
<title>Corvella Marine – Business Card</title>
<link href="https://fonts.googleapis.com/css2?family=Montserrat:wght@400;500;700&display=swap" rel="stylesheet">
<style>
  :root {
    --backdrop: #4b5052;
    --blue: #0b55a3;
    --orange: #f07322;
    --white: #ffffff;
  }
  * { margin: 0; padding: 0; box-sizing: border-box; }
  html, body { width: 1200px; height: 1050px; overflow: hidden; }
  body {
    background: var(--backdrop);
    font-family: "Montserrat", sans-serif;
    position: relative;
  }
  .card {
    position: absolute;
    width: 540px;
    height: 310px;
    overflow: hidden;
  }
  /* Front: contact side */
  .card--front { left: 40px; top: 370px; background: var(--blue); }
  .band { position: absolute; left: 0; width: 100%; background: var(--orange); }
  .band--name { top: 20px; height: 58px; }
  .band--address { top: 232px; height: 58px; }
  .holder-name {
    position: absolute; left: 140px; top: 35px;
    color: var(--white); font-weight: 700; font-size: 22px;
    letter-spacing: 3px; text-transform: uppercase;
  }
  .icon-strip {
    position: absolute; left: 36px; top: 86px;
    width: 34px; height: 128px; background: var(--white);
    display: flex; flex-direction: column; align-items: center;
    justify-content: space-around; padding: 4px 0;
  }
  .icon-strip svg { width: 18px; height: 18px; }
  .contact-list {
    position: absolute; left: 96px; top: 88px;
    list-style: none; color: var(--white);
    font-size: 15px; line-height: 24px; font-weight: 400;
  }
  .address-block {
    position: absolute; left: 18px; top: 238px;
    display: flex; align-items: center; gap: 14px;
    color: var(--white); font-size: 15px; line-height: 22px;
  }
  .address-block .divider { width: 1.5px; height: 40px; background: var(--white); }
  .brand-front {
    position: absolute; right: 28px; top: 132px;
    display: flex; align-items: center; gap: 10px;
    color: var(--white); font-weight: 700; font-size: 20px;
    text-transform: uppercase; letter-spacing: 1px;
  }
  .brand-dot { width: 22px; height: 22px; border-radius: 50%; background: var(--orange); flex: none; }

  /* Back: logo side */
  .card--back {
    left: 620px; top: 370px; background: var(--white);
    display: flex; flex-direction: column; align-items: center; justify-content: center; gap: 18px;
  }
  .brand-back-mark { width: 64px; height: 64px; border-radius: 50%; background: var(--orange); }
  .brand-back-name {
    color: var(--blue); font-weight: 700; font-size: 34px;
    text-transform: uppercase; letter-spacing: 2px;
  }
</style>
</head>
<body>
  <section class="card card--front" aria-label="Business card front">
    <div class="band band--name"></div>
    <div class="band band--address"></div>
    <h1 class="holder-name">Dale Pritchett</h1>

    <div class="icon-strip" aria-hidden="true">
      <svg viewBox="0 0 20 20"><path d="M5 2h3l1 5-2 1.5c1 2 2.5 3.5 4.5 4.5L13 11l5 1v3c0 1-1 2-2 2C8.5 17 3 11.5 3 4c0-1 1-2 2-2z" fill="var(--blue)"/></svg>
      <svg viewBox="0 0 20 20"><rect x="2" y="4" width="16" height="12" fill="none" stroke="var(--blue)" stroke-width="1.6"/><path d="M2 4l8 7 8-7" fill="none" stroke="var(--blue)" stroke-width="1.6"/></svg>
      <svg viewBox="0 0 20 20"><circle cx="10" cy="10" r="8" fill="none" stroke="var(--blue)" stroke-width="1.6"/><ellipse cx="10" cy="10" rx="3.5" ry="8" fill="none" stroke="var(--blue)" stroke-width="1.3"/><path d="M2 10h16M3.5 6h13M3.5 14h13" stroke="var(--blue)" stroke-width="1.2"/></svg>
      <svg viewBox="0 0 20 20"><rect x="5" y="1.5" width="10" height="17" rx="1.5" fill="none" stroke="var(--blue)" stroke-width="1.6"/><rect x="7" y="4" width="6" height="5" fill="var(--blue)"/><path d="M7 12h2M11 12h2M7 15h2M11 15h2" stroke="var(--blue)" stroke-width="1.5"/></svg>
      <svg viewBox="0 0 20 20"><rect x="5" y="2" width="10" height="6" fill="none" stroke="var(--blue)" stroke-width="1.5"/><rect x="2" y="8" width="16" height="7" fill="var(--blue)"/><rect x="5" y="13" width="10" height="5" fill="var(--white)" stroke="var(--blue)" stroke-width="1.5"/></svg>
    </div>

    <ul class="contact-list">
      <li>954-382-7146</li>
      <li>212@corvellamarine.com</li>
      <li>corvellamarine.com</li>
      <li>54-451-8320</li>
      <li>954:382-7139</li>
    </ul>

    <div class="brand-front">
      <span class="brand-dot"></span>
      <span>Corvella Marine</span>
    </div>

    <div class="address-block">
      <svg width="22" height="30" viewBox="0 0 22 30" aria-hidden="true">
        <path d="M11 2a7 7 0 0 1 7 7c0 5-7 12-7 12S4 14 4 9a7 7 0 0 1 7-7z" fill="none" stroke="var(--white)" stroke-width="2"/>
        <circle cx="11" cy="9" r="2.5" fill="var(--white)"/>
        <ellipse cx="11" cy="26" rx="8" ry="2.5" fill="none" stroke="var(--white)" stroke-width="1.6"/>
      </svg>
      <span class="divider"></span>
      <p>Address: 718 West Halden Lane,<br>Dania Beach, FL 33019</p>
    </div>
  </section>

  <section class="card card--back" aria-label="Business card back">
    <span class="brand-back-mark"></span>
    <span class="brand-back-name">Corvella Marine</span>
  </section>
</body>
</html>
```